Brannigan Schedule Oversight Group Inc. needs a logo design (BSOGI) and a business card design

We need a logo design and business card design for a new company. Simple yet elegant/stylish and professional. to the point. Focal point BRANNIGAN...underneith Schedule Oversight Group Inc smaller font. Plus a logo that can be on the opposite side of the business card and used for T-Shirts.
Back back ground, silver/grey font. I like the look of QVR Design logo
Target Market(s)
Project controls, Planning, Scheduling, Engineering, Project Management
Industry/Entity Type
Business
Contact Information for Business Card
Company name on one side, logo and details on the other
Font styles to use
Requirements
Must have
- Rosalind Brannigan
- Project Planner
- BranniganSOGI@mailnest.example
- P.O. Box 7
- Fernhollow NR CANADA
- T0M2J3
- +1 (403) 555 0187
Nice to have
- Your input :) quote "Fail to plan, plan to fail"
Should not have
- Too much!

```html
<!DOCTYPE html>
<html lang="en">
<head>
<meta charset="utf-8">
<title>Brannigan Schedule Oversight Group Inc. – Business Card</title>
<link rel="stylesheet" href="https://fonts.googleapis.com/css2?family=Arimo:wght@400;700&display=swap">
<style>
  :root {
    --backdrop: #9a9a9a;
    --card: #1c1c1c;
    --silver: #d6d8da;
    --silver-soft: #a9abad;
    --grey-text: #8a8a8a;
    --rule: #c9cbcd;
  }
  * { box-sizing: border-box; margin: 0; padding: 0; }
  html, body {
    width: 1200px; height: 924px; overflow: hidden;
    background: var(--backdrop);
    font-family: "Arimo", Arial, sans-serif;
  }
  .sheet {
    width: 1200px; height: 924px;
    display: flex; flex-direction: column; align-items: center; justify-content: center;
    gap: 44px;
  }
  .card {
    width: 690px; height: 394px;
    background: var(--card);
    border-radius: 22px;
    position: relative;
    color: var(--silver);
    overflow: hidden;
  }
  .wordmark { display: flex; flex-direction: column; align-items: center; }
  .wordmark__name {
    font-weight: 700; color: var(--silver); letter-spacing: -1px; line-height: 1;
  }
  .wordmark__tag {
    display: flex; align-items: center; gap: 14px;
    color: var(--silver); font-weight: 700; text-transform: uppercase; letter-spacing: 0.5px;
  }
  .wordmark__tag::before, .wordmark__tag::after {
    content: ""; height: 2px; background: var(--rule);
  }
  .card--front { display: flex; align-items: center; justify-content: center; }
  .card--front .wordmark__name { font-size: 96px; }
  .card--front .wordmark__tag { font-size: 17px; margin-top: 6px; }
  .card--front .wordmark__tag::before, .card--front .wordmark__tag::after { width: 44px; }

  .card--back .wordmark { position: absolute; top: 42px; left: 0; right: 0; }
  .card--back .wordmark__name { font-size: 60px; }
  .card--back .wordmark__tag { font-size: 14px; margin-top: 4px; }
  .card--back .wordmark__tag::before, .card--back .wordmark__tag::after { width: 40px; }

  .holder {
    position: absolute; left: 56px; top: 196px; width: 300px; text-align: right;
  }
  .holder__name { font-size: 25px; font-weight: 700; color: var(--silver-soft); }
  .holder__role { font-size: 19px; color: var(--grey-text); margin-top: 4px; }
  .holder__quote { font-size: 19px; color: var(--grey-text); margin-top: 62px; }

  .divider {
    position: absolute; left: 386px; top: 190px; width: 2px; height: 150px; background: var(--rule);
  }
  .contact {
    position: absolute; left: 410px; right: 30px; top: 196px; list-style: none;
    font-size: 14px; color: var(--silver-soft); line-height: 1.35;
  }
  .contact li { display: flex; gap: 9px; margin-bottom: 6px; }
  .contact svg { flex: none; width: 16px; height: 16px; margin-top: 1px; }
</style>
</head>
<body>
  <main class="sheet">
    <section class="card card--front" aria-label="Card front">
      <div class="wordmark">
        <span class="wordmark__name">Brannigan</span>
        <span class="wordmark__tag">Schedule Oversight Group Inc</span>
      </div>
    </section>

    <section class="card card--back" aria-label="Card back">
      <div class="wordmark">
        <span class="wordmark__name">Brannigan SOGI</span>
        <span class="wordmark__tag">Schedule Oversight Group Inc</span>
      </div>

      <div class="holder">
        <p class="holder__name">Rosalind Brannigan</p>
        <p class="holder__role">Project Planner</p>
        <p class="holder__quote">"Fail to plan, plan to fail"</p>
      </div>

      <div class="divider"></div>

      <ul class="contact">
        <li>
          <svg viewBox="0 0 16 16" aria-hidden="true"><rect width="16" height="16" rx="2" fill="#d6d8da"/><path d="M5 3.5l1.6 2.2-1 1.2a6 6 0 0 0 3.3 3.3l1.2-1 2.2 1.6-.9 1.7C7.6 12.5 3.5 8.4 3.5 4.4z" fill="#1c1c1c"/></svg>
          <span>+1 403 555 0187</span>
        </li>
        <li>
          <svg viewBox="0 0 16 16" aria-hidden="true"><rect width="16" height="16" rx="2" fill="#d6d8da"/><rect x="3" y="4.5" width="10" height="7" fill="#1c1c1c"/><path d="M3 4.5l5 4 5-4" stroke="#d6d8da" stroke-width="1" fill="none"/></svg>
          <span>BranniganSOGI@mailnest.example</span>
        </li>
        <li>
          <svg viewBox="0 0 16 16" aria-hidden="true"><rect width="16" height="16" rx="2" fill="#d6d8da"/><path d="M8 2.8a3.6 3.6 0 0 0-3.6 3.6C4.4 9 8 13.2 8 13.2s3.6-4.2 3.6-6.8A3.6 3.6 0 0 0 8 2.8z" fill="#1c1c1c"/><circle cx="8" cy="6.4" r="1.3" fill="#d6d8da"/></svg>
          <span>P.O. Box 7<br>Fernhollow NR CANADA<br>T0M2J3</span>
        </li>
      </ul>
    </section>
  </main>
</body>
</html>
```